Flyer für selbstständigen Finanzierungsvermittler  für Baufinanzierungen
Flyer für selbstständigen Finanzierungsvermittler für Baufinanzierungen
Zielgruppe
seit 1999 selbstständiger Finanzierungsvermittler für Baufinanzierungen.
ich arbeite für (nicht angestellt) ein Maklerbüro in Schorndorf, hier wurde vor Jahren ein Flyer konzepiert.
Zukünftiger Flyer soll von Immobilienmaklern Interessenten ausgehändigt oder in Kundenmappe VEK-Maklerbüro beigelegt werden.
Aufgabenstellung
- der beigefügte Flyer von Lukas Brandel hat schon sehr viel von dem, was ich mir das vorstelle
- die Farben des Maklerbüros sind Blau und weiß, kann aber auch ganz anders entworfen werden
- Es soll ein DinA 4 Flyer werden, ebenso die PDF-Datei hierzu
- Adressfeld: Stefan Kurlen, Baufinanzierungsspezialist, Bankkaufmann, Haldenweg 17, 73814 Remsfelden, Mobil 0171 546 7183, stefan@kurlen48.de
Text für den Flyer, anlehnend an beileigende:
- Längjährige Erfahrung
- Vergleich von über 300 Banken
- Top Konditionen, bis zu 40 Jahre Zinsbindung
- Beratung vor Ort, auch per Viseo und Telefon möglich
- rasche Zusage, aufgrund persönlichem Kontakt zu Entscheidungsträgern der Bank
mitgelieferte Bilder dürfen natürlich zugeschnitten werden (nur bis Brust) oder weniger Hintergrund, etc.

```html
<!DOCTYPE html>
<html lang="de">
<head>
<meta charset="utf-8">
<title>Flyer Stefan Kurlen – Baufinanzierung</title>
<link rel="stylesheet" href="https://fonts.googleapis.com/css2?family=Open+Sans:wght@400;600&family=Raleway:wght@400;500&display=swap">
<style>
  :root {
    --page-bg: #ffffff;
    --charcoal: #3f3d3e;
    --petrol: #0a5a7e;
    --line-blue: #1a6fc4;
    --name-blue: #0e5779;
    --accent-blue: #1f7fc1;
    --ink: #1d1d1b;
    --muted-white: #a9bfcf;
    --white: #ffffff;
  }
  html, body {
    margin: 0;
    padding: 0;
    width: 1200px;
    height: 2382px;
    overflow: hidden;
    background: var(--page-bg);
  }
  .flyer {
    position: absolute;
    left: 59px;
    top: 425px;
    width: 801px;
    height: 1134px;
    transform: scale(1.35);
    transform-origin: 0 0;
    background: var(--white);
    box-shadow: 0 10px 40px rgba(0,0,0,0.18);
    overflow: hidden;
    font-family: "Open Sans", sans-serif;
  }
  .flyer-shapes { position: absolute; inset: 0; }
  .brand {
    position: absolute;
    left: 62px;
    top: 40px;
    display: flex;
    align-items: center;
    gap: 18px;
  }
  .brand-dot {
    width: 24px; height: 24px;
    border: 1.5px solid var(--white);
    border-radius: 50%;
  }
  .brand-name {
    color: var(--white);
    font-size: 11px;
    font-weight: 600;
    letter-spacing: 2px;
  }
  .advisor-name {
    position: absolute;
    right: 56px;
    top: 178px;
    margin: 0;
    text-align: right;
    color: var(--name-blue);
    font-weight: 400;
    font-size: 60px;
    line-height: 62px;
    letter-spacing: 1px;
  }
  .contact {
    position: absolute;
    right: 58px;
    top: 368px;
    text-align: right;
    color: var(--ink);
    font-size: 11.5px;
    line-height: 16px;
  }
  .contact-title {
    color: var(--accent-blue);
    font-weight: 600;
    font-size: 10.5px;
    margin: 0 0 15px;
  }
  .contact p { margin: 0; }
  .contact .role { margin-bottom: 17px; }
  .benefit {
    position: absolute;
    transform: translateX(-50%);
    text-align: center;
    font-family: "Raleway", sans-serif;
    text-transform: uppercase;
    white-space: nowrap;
  }
  .benefit-main {
    top: 700px;
    color: var(--white);
    font-size: 20px;
    line-height: 29px;
    font-weight: 500;
  }
  .benefit-main svg { display: block; margin: 0 auto 12px; }
  .benefit-sub {
    top: 888px;
    color: var(--muted-white);
    font-size: 14.5px;
    line-height: 20px;
    font-weight: 500;
    letter-spacing: 0.3px;
  }
  .benefit-sub svg { display: block; margin: 0 auto 10px; }
</style>
</head>
<body>
<main class="flyer">
  <svg class="flyer-shapes" width="801" height="1134" viewBox="0 0 801 1134">
    <defs>
      <linearGradient id="portraitTone" x1="0" y1="0" x2="1" y2="1">
        <stop offset="0" stop-color="#c9d8e2"/>
        <stop offset="0.55" stop-color="#e6edf2"/>
        <stop offset="1" stop-color="#3a3a3c"/>
      </linearGradient>
    </defs>
    <polygon class="portrait-area" role="img" aria-label="Porträtfoto des Finanzierungsberaters im Anzug" points="0,107 340,143 505,495 0,713" fill="url(#portraitTone)"/>
    <polygon class="header-band" points="0,0 512,0 340,143 0,107" fill="var(--charcoal)"/>
    <polygon class="info-band" points="0,713 505,495 801,718 801,1134 0,1134" fill="var(--petrol)"/>
    <g class="accent-lines" fill="none" stroke="var(--line-blue)" stroke-width="1.2">
      <polyline points="0,107 340,143 512,0"/>
      <line x1="340" y1="143" x2="728" y2="0"/>
      <line x1="340" y1="143" x2="505" y2="495"/>
      <line x1="505" y1="495" x2="801" y2="650"/>
      <polyline points="110,1134 574,1055 801,1115"/>
    </g>
  </svg>

  <div class="brand">
    <span class="brand-dot"></span>
    <span class="brand-name">IHR BAUFINANZIERUNGSSPEZIALIST</span>
  </div>

  <h1 class="advisor-name">STEFAN<br>KURLEN</h1>

  <section class="contact">
    <p class="contact-title">KONTAKT</p>
    <p class="role">Stefan Kurlen &nbsp;|&nbsp; Bankkaufmann</p>
    <p>Haldenweg 17 &nbsp;|&nbsp; 73814 Remsfelden</p>
    <p>Mobil 0171 546 7183</p>
    <p>stefan@kurlen48.de</p>
  </section>

  <div class="benefit benefit-main" style="left:176px">
    <svg width="46" height="30" viewBox="0 0 46 30"><path d="M2 17 L14 27 L44 3" fill="none" stroke="#fff" stroke-width="5" stroke-linecap="round" stroke-linejoin="round"/></svg>
    LÄNGJÄHRIGE<br>ERFAHRUNG
  </div>
  <div class="benefit benefit-main" style="left:376px">
    <svg width="46" height="30" viewBox="0 0 46 30"><path d="M2 17 L14 27 L44 3" fill="none" stroke="#fff" stroke-width="5" stroke-linecap="round" stroke-linejoin="round"/></svg>
    VERGLEICH<br>VON ÜBER<br>300 BANKEN
  </div>
  <div class="benefit benefit-main" style="left:604px">
    <svg width="46" height="30" viewBox="0 0 46 30"><path d="M2 17 L14 27 L44 3" fill="none" stroke="#fff" stroke-width="5" stroke-linecap="round" stroke-linejoin="round"/></svg>
    TOP KONDITIONEN<br>BIS ZU 40 JAHRE<br>ZINSBINDUNG
  </div>

  <div class="benefit benefit-sub" style="left:230px">
    <svg width="38" height="34" viewBox="0 0 38 34" fill="none" stroke="#a9bfcf" stroke-width="1.5"><path d="M19 2 C29 2 36 8 36 16 C36 24 29 30 19 30 C16 30 13 29 11 28 L3 32 L6 25 C3 22 2 19 2 16 C2 8 9 2 19 2 Z"/><path d="M11 11 H27 M11 15 H27 M11 19 H27 M11 23 H24"/></svg>
    BERATUNG VOR ORT<br>AUCH PER VIDEO UND<br>TELEFON MÖGLICH
  </div>
  <div class="benefit benefit-sub" style="left:522px">
    <svg width="42" height="36" viewBox="0 0 42 36" fill="none" stroke="#a9bfcf" stroke-width="1.5"><rect x="2" y="6" width="24" height="28" rx="1"/><rect x="9" y="3" width="10" height="5"/><path d="M6 14 H20 M6 19 H18 M6 24 H16 M6 29 H14"/><path d="M24 26 L38 6 L41 8 L27 28 L23 30 Z"/></svg>
    RASCHE ZUSAGE, AUFGRUND<br>PERSÖNLICHEM KONTAKT ZU<br>ENTSCHEIDUNGSTRÄGERN DER BANK
  </div>
</main>
</body>
</html>
```